Non-fiction book about The Lanternkeeper, needs cover design

This book is about me, and a lifetime of abuse that I survived. The goal is to help others in abusive situations break the cycle of shame that accompanies unhealthy and toxic relationships. I want the cover to illustrate a vast and sometimes scary world where we victims feel alone. It's up to us to choose our destiny, and sometimes we must do that when others don't agree. But there is hope. No longer do we need to believe the lie that something broken is better than nothing at all. After reading this, others will learn to trust their intuition, and how to avoid the pitfalls and red flags of toxic relationships. I want the cover to also show strength, hope, and positivity in the face of adversity. The picture of me (attached) is a good start to show a great big and sometimes frightening world a victim of abuse lives in. I love nature photos, but it's not a requirement for this project. I prefer simple designs. Thank you so much!

Target Market(s)

Survivors of abuse, at risk youth, and friends/family with loved ones who are abused

Requirements
Must have
• Title: The Lanternkeeper
Quit Trading Your Peace for a Cracked Promise That Holds You Back Forever: Quit Trading Your Peace for a Cracked Promise That Holds You Back Forever
Nice to have
• Outdoor scenery, open spaces.

```html
<!DOCTYPE html>
<html lang="en">
<head>
<meta charset="utf-8">
<title>The Lanternkeeper — Cover Wrap</title>
<link href="https://fonts.googleapis.com/css2?family=Playfair+Display:ital,wght@0,400;1,400;1,500&family=PT+Serif&display=swap" rel="stylesheet">
<style>
  :root {
    --page-bg: #f1f1f1;
    --paper: #ffffff;
    --ink: #111111;
    --title-blue: #1a72c0;
    --art-top: #8a6a52;
    --art-mid: #f1ece6;
    --art-low: #8e3c2f;
  }
  html, body {
    margin: 0;
    padding: 0;
    width: 899px;
    height: 1200px;
    overflow: hidden;
    background: var(--page-bg);
  }
  .cover-wrap {
    position: absolute;
    left: 20px;
    top: 303px;
    width: 860px;
    height: 594px;
    background: var(--paper);
    box-shadow: 0 2px 8px rgba(0,0,0,0.35);
    overflow: hidden;
  }
  .book-title { margin: 0; }
  .title-line {
    position: absolute;
    display: block;
    font-family: "Playfair Display", serif;
    font-style: italic;
    font-weight: 500;
    color: var(--title-blue);
    line-height: 1;
    white-space: nowrap;
  }
  .title-line .article { font-weight: 400; }
  .rule {
    position: absolute;
    background: var(--title-blue);
  }

  /* Back cover */
  .back-title-top { left: 78px; top: 30px; font-size: 46px; }
  .back-title-top .article { font-size: 21px; }
  .back-title-bottom { left: 150px; top: 74px; font-size: 50px; }
  .back-rule { left: 60px; top: 130px; width: 285px; height: 4px; }
  .blurb {
    position: absolute;
    left: 51px;
    top: 148px;
    width: 290px;
    margin: 0;
    font-family: "PT Serif", serif;
    font-size: 11px;
    line-height: 13.6px;
    color: var(--ink);
    text-align: justify;
    hyphens: auto;
  }

  /* Spine */
  .spine-title {
    position: absolute;
    left: 432px;
    top: 218px;
    transform: translate(-50%, -50%) rotate(-90deg);
    font-family: "Playfair Display", serif;
    font-style: italic;
    font-weight: 500;
    font-size: 36px;
    color: var(--title-blue);
    white-space: nowrap;
    line-height: 1;
  }
  .spine-author {
    position: absolute;
    left: 432px;
    top: 485px;
    transform: translate(-50%, -50%) rotate(-90deg);
    font-family: "Playfair Display", serif;
    font-size: 12px;
    letter-spacing: 0.3em;
    color: var(--ink);
    white-space: nowrap;
  }

  /* Front cover */
  .front-author {
    position: absolute;
    left: 463px;
    width: 397px;
    top: 22px;
    text-align: center;
    font-family: "Playfair Display", serif;
    font-size: 25px;
    letter-spacing: 0.3em;
    color: var(--ink);
    margin: 0;
  }
  .front-art {
    position: absolute;
    left: 557px;
    top: 78px;
    width: 204px;
    height: 251px;
    border-radius: 46% 40% 30% 34% / 30% 34% 26% 30%;
    background: linear-gradient(180deg, var(--art-top) 0%, var(--art-top) 22%, var(--art-mid) 40%, var(--art-mid) 58%, var(--art-low) 72%, var(--art-low) 100%);
  }
  .front-title-top { left: 500px; top: 345px; font-size: 70px; }
  .front-title-top .article { font-size: 31px; }
  .front-title-bottom { left: 610px; top: 414px; font-size: 76px; }
  .front-rule { left: 463px; top: 502px; width: 397px; height: 5px; }
  .front-subtitle {
    position: absolute;
    left: 483px;
    width: 357px;
    top: 518px;
    margin: 0;
    font-family: "Playfair Display", serif;
    font-style: italic;
    font-size: 19px;
    line-height: 24px;
    letter-spacing: 0.02em;
    text-align: center;
    color: var(--ink);
  }
</style>
</head>
<body>
  <main class="cover-wrap">
    <section class="back-cover">
      <h2 class="book-title">
        <span class="title-line back-title-top"><span class="article">The </span>Lantern</span>
        <span class="title-line back-title-bottom">keeper</span>
      </h2>
      <div class="rule back-rule"></div>
      <p class="blurb">Lorem ipsum dolor sit amet, consectetur adipiscing elit. Quisque non odio vitae metus iaculis aliquet in sed erat. Donec id lectus risus. Proin non orci gravida, interdum odio non, dapibus justo. Suspendisse aliquet lacus volutpat tortor volutpat hendrerit. Etiam quis pharetra metus. Maecenas finibus viverra mauris, at lacinia mi malesuada in. Donec finibus, mauris non suscipit aliquet, neque ante consequat nulla, et sodales orci neque vel mauris. Donec auctor arcu quis malesuada euismod. Suspendisse sit amet tempor leo, a tempus metus. Quisque porta semper placerat. Proin nec condimentum sem. Cras dictum pulvinar enim sed rutrum. Suspendisse commodo sapien nec lacus accumsan semper. Nulla commodo, nisl eget pulvinar imperdiet, tellus tellus ultrices dui, ut imperdiet risus lorem ac ipsum.</p>
    </section>

    <section class="spine">
      <div class="spine-title">The Lanternkeeper</div>
      <div class="spine-author">author name</div>
    </section>

    <section class="front-cover">
      <p class="front-author">author name</p>
      <div class="front-art" role="img" aria-label="Painted illustration of a seated figure hunched over, seen from behind, in brown, white and deep red tones"></div>
      <h1 class="book-title">
        <span class="title-line front-title-top"><span class="article">The </span>Lantern</span>
        <span class="title-line front-title-bottom">keeper</span>
      </h1>
      <div class="rule front-rule"></div>
      <p class="front-subtitle">Quit Trading Your Peace for a Cracked Promise That Holds You Back Forever</p>
    </section>
  </main>
</body>
</html>
```